Personal training studio poster / postcard

We need a poster / postcard design to advertise our recently established personal training studio - details and logo in the attached file. Logo file also provided.

We are flexible on format. Prefer the use of pictures in the design.

Training

```html
<!DOCTYPE html>
<html lang="en">
<head>
<meta charset="UTF-8">
<title>Kestrel Strength Studio – Class Timetable</title>
<link rel="stylesheet" href="https://fonts.googleapis.com/css2?family=Michroma&display=swap">
<style>
  :root {
    --bg-deep: #111114;
    --bg-mid: #1d1d22;
    --accent-red: #e0141c;
    --text-white: #f2f2f2;
    --text-silver: #d4d4d8;
    --panel-fill: rgba(10, 10, 12, 0.78);
    --panel-edge: #55555c;
    --photo-light: #b4b4b8;
    --photo-mid: #6a6a70;
    --photo-dark: #2a2a2f;
  }
  * { margin: 0; padding: 0; box-sizing: border-box; }
  html, body { width: 853px; height: 1200px; overflow: hidden; background: var(--bg-deep); }
  .poster {
    position: relative;
    width: 853px;
    height: 1200px;
    overflow: hidden;
    background: linear-gradient(160deg, var(--bg-mid) 0%, var(--bg-deep) 55%, #0c0c0f 100%);
    font-family: "Michroma", "Arial", sans-serif;
  }
  .facets, .accent-lines { position: absolute; inset: 0; }
  .brand {
    position: absolute;
    top: 200px;
    left: 0;
    width: 853px;
    text-align: center;
    color: var(--text-silver);
    letter-spacing: 2px;
  }
  .brand-name { font-size: 54px; line-height: 1.1; }
  .brand-sub { font-size: 26px; line-height: 1.4; letter-spacing: 4px; }
  .schedule-panel {
    position: absolute;
    left: 43px;
    top: 489px;
    width: 762px;
    height: 320px;
    background: var(--panel-fill);
    border: 1px solid var(--panel-edge);
  }
  .athlete-photo {
    position: absolute;
    left: 500px;
    top: 335px;
    width: 290px;
    height: 865px;
    border-radius: 120px 120px 60px 60px;
    background: linear-gradient(180deg, var(--photo-light) 0%, var(--photo-mid) 40%, var(--photo-dark) 100%);
    opacity: 0.9;
  }
  .schedule {
    position: absolute;
    left: 57px;
    top: 552px;
    list-style: none;
  }
  .schedule-item {
    font-size: 18px;
    line-height: 75px;
    color: var(--text-white);
    text-transform: uppercase;
    white-space: nowrap;
  }
  .class-name { color: var(--accent-red); }
</style>
</head>
<body>
<div class="poster">
  <svg class="facets" width="853" height="1200" viewBox="0 0 853 1200">
    <polygon points="0,0 560,0 300,420 0,260" fill="#18181c"/>
    <polygon points="560,0 853,0 853,260 700,120" fill="#202026"/>
    <polygon points="0,780 300,900 0,1200" fill="#17171b"/>
    <polygon points="300,900 500,1000 420,1200 0,1200" fill="#141418"/>
  </svg>

  <div class="brand">
    <div class="brand-name">KESTREL</div>
    <div class="brand-sub">STRENGTH STUDIO</div>
  </div>

  <div class="schedule-panel"></div>

  <svg class="accent-lines" width="853" height="1200" viewBox="0 0 853 1200">
    <polyline points="745,0 853,78" fill="none" stroke="var(--accent-red)" stroke-width="3"/>
    <polyline points="0,1040 242,936 853,1125" fill="none" stroke="var(--accent-red)" stroke-width="3"/>
  </svg>

  <div class="athlete-photo" role="img" aria-label="Black and white photo of a female athlete in sports wear holding a dumbbell"></div>

  <ul class="schedule">
    <li class="schedule-item"><span class="class-name">Power Circuit</span> – Tuesdays 6:15am</li>
    <li class="schedule-item"><span class="class-name">Boxing + MMA</span> – Tuesdays and Thursdays 6:15pm</li>
    <li class="schedule-item"><span class="class-name">Yoga</span> – Saturdays 9am</li>
  </ul>
</div>
</body>
</html>
```